New business card for civil engineering company - "Keel Survey"

We need a business card designed for our new structural engineering company.

The company name is "Keel Survey" logo files attached.

We would like the following:
* Two-sided card
* Simple design

Information to be placed on the card:
Name - Marcus Hollby
Job Title - Director / Structural Engineer
Credentials - BEng(Hons), CPEng, CMengNZ, IntPE(NZ)
Email - marcus.hollby@keelsurvey-example.co.nz
mobile - 0219036458
website - www.keelsurvey-example.co.nz

```html
<!DOCTYPE html>
<html lang="en">
<head>
<meta charset="utf-8">
<title>Keel Survey – Business Card</title>
<link href="https://fonts.googleapis.com/css2?family=Exo+2:ital,wght@0,400;0,600;0,700;1,400&family=Open+Sans:wght@400&display=swap" rel="stylesheet">
<style>
  :root {
    --backdrop: #3a3b3e;
    --card: #1e1f23;
    --ink: #ffffff;
    --sky: #8fbce8;
    --sky-deep: #5e95d6;
    --navy: #1d3f78;
    --mid-blue: #2f63a8;
    --icon: #6fa7e0;
  }
  * { margin: 0; padding: 0; box-sizing: border-box; }
  html, body {
    width: 799px; height: 1200px; overflow: hidden;
    background: var(--backdrop);
  }
  .sheet {
    width: 799px; height: 1200px;
    display: flex; flex-direction: column; align-items: center; justify-content: center;
    gap: 90px;
  }
  .card {
    position: relative;
    width: 640px; height: 391px;
    background: var(--card);
    border-radius: 4px;
    overflow: hidden;
    box-shadow: 0 10px 30px rgba(0,0,0,0.45);
  }
  .wordmark {
    display: flex; align-items: center; gap: 12px;
    font-family: "Exo 2", sans-serif;
    font-weight: 600;
    color: var(--ink);
    letter-spacing: 2px;
    text-transform: uppercase;
    white-space: nowrap;
  }
  .wordmark .mark-square {
    width: 22px; height: 22px; background: var(--sky-deep);
  }
  .card-front .wordmark {
    position: absolute; left: 50%; top: 50%;
    transform: translate(-50%, -50%);
    font-size: 38px;
  }
  .card-back .wordmark {
    position: absolute; left: 40px; top: 200px;
    font-size: 30px;
  }
  .card-back .wordmark .mark-square { width: 18px; height: 18px; }
  .swoosh { position: absolute; inset: 0; width: 100%; height: 100%; }
  .person {
    position: absolute; right: 38px; top: 74px;
    text-align: right; color: var(--ink);
    font-family: "Exo 2", sans-serif;
  }
  .person .name { font-size: 26px; font-weight: 700; letter-spacing: 0.5px; }
  .person .role { font-size: 14px; font-style: italic; margin-top: 2px; }
  .person .credentials { font-size: 14px; line-height: 1.3; margin-top: 2px; }
  .contact {
    position: absolute; right: 30px; top: 308px;
    list-style: none;
    font-family: "Open Sans", sans-serif;
    font-size: 14px; color: var(--ink);
  }
  .contact li {
    display: flex; justify-content: flex-end; align-items: center; gap: 12px;
    height: 22px; white-space: nowrap;
  }
  .contact svg { width: 14px; height: 14px; fill: var(--icon); flex: none; }
</style>
</head>
<body>
<main class="sheet">
  <section class="card card-front" aria-label="Card front">
    <div class="wordmark"><span class="mark-square"></span>Keel Survey</div>
  </section>

  <section class="card card-back" aria-label="Card back">
    <svg class="swoosh" viewBox="0 0 640 391" aria-hidden="true">
      <defs>
        <linearGradient id="panelFill" x1="0" y1="0" x2="1" y2="1">
          <stop offset="0" stop-color="#5b93d4"/>
          <stop offset="0.5" stop-color="#2f63a8"/>
          <stop offset="1" stop-color="#1b3a70"/>
        </linearGradient>
      </defs>
      <!-- blue panel above the sweep -->
      <path d="M120,14 C280,14 380,70 430,155 C480,240 540,285 640,290 L640,0 L120,0 Z" fill="url(#panelFill)"/>
      <!-- blue edge band following the sweep -->
      <path d="M110,20 C280,20 380,76 430,161 C480,246 540,291 640,296" fill="none" stroke="#2f63a8" stroke-width="16"/>
      <!-- dark gap line running the full sweep -->
      <path d="M110,20 C280,20 380,76 430,161 C480,246 540,291 640,296" fill="none" stroke="#1e1f23" stroke-width="5"/>
      <!-- light arc from the left edge rising into the top -->
      <path d="M0,44 C60,22 130,10 230,8" fill="none" stroke="#8fbce8" stroke-width="9" stroke-linecap="butt"/>
    </svg>

    <div class="wordmark"><span class="mark-square"></span>Keel Survey</div>

    <div class="person">
      <p class="name">Marcus Hollby</p>
      <p class="role">Director / Structural Engineer</p>
      <p class="credentials">BEng(Hons), CPEng,<br>CMengNZ, IntPE(NZ)</p>
    </div>

    <ul class="contact">
      <li>0219036458
        <svg viewBox="0 0 24 24" aria-hidden="true"><path d="M6.6 10.8a15 15 0 0 0 6.6 6.6l2.2-2.2c.3-.3.7-.4 1-.2 1.1.4 2.3.6 3.6.6.6 0 1 .4 1 1V20c0 .6-.4 1-1 1A17 17 0 0 1 3 4c0-.6.4-1 1-1h3.5c.6 0 1 .4 1 1 0 1.3.2 2.5.6 3.6.1.3 0 .7-.2 1z"/></svg>
      </li>
      <li>www.keelsurvey-example.co.nz
        <svg viewBox="0 0 24 24" aria-hidden="true"><path d="M12 2a10 10 0 1 0 0 20 10 10 0 0 0 0-20zm6.9 6h-3a15 15 0 0 0-1.4-3.6A8 8 0 0 1 18.9 8zM12 4c.8 1.2 1.5 2.5 1.9 4h-3.8c.4-1.5 1.1-2.8 1.9-4zM4.3 14a8 8 0 0 1 0-4h3.4a16 16 0 0 0 0 4zm.8 2h3a15 15 0 0 0 1.4 3.6A8 8 0 0 1 5.1 16zm3-8h-3a8 8 0 0 1 4.4-3.6C8.9 5.5 8.4 6.7 8.1 8zM12 20c-.8-1.2-1.5-2.5-1.9-4h3.8c-.4 1.5-1.1 2.8-1.9 4zm2.3-6H9.7a14 14 0 0 1 0-4h4.6a14 14 0 0 1 0 4zm.2 5.6c.6-1.1 1.1-2.3 1.4-3.6h3a8 8 0 0 1-4.4 3.6zM16.3 14a16 16 0 0 0 0-4h3.4a8 8 0 0 1 0 4z"/></svg>
      </li>
      <li>marcus.hollby@keelsurvey-example.co.nz
        <svg viewBox="0 0 24 24" aria-hidden="true"><path d="M2 5h20v14H2zm2 2v.5l8 5 8-5V7zm0 2.8V17h16V9.8l-8 5z"/></svg>
      </li>
    </ul>
  </section>
</main>
</body>
</html>
```